Bookcover: Lessons From the Silent Orchard

I am publishing a super-low-cost innovation book for €4,99 on Bravolo Self Release to help everyone become a great innovator: young ambitious people without college education nor a big budget. Do you want to help me?

Brief:
Design a book cover 1600 x 2560 pixels for BSR.
Main title: Lessons From the Silent Orchard
Sub title: mindset - insights - skills & tools
Author: Maarten de Klerk
Design: captive, and appealing to everyone
Target Group: young ambitious people without college education

For bravolo please format the height/width ratio of 1.6:1

```html
<!DOCTYPE html>
<html lang="en">
<head>
<meta charset="utf-8">
<title>Lessons From the Silent Orchard — Book Cover</title>
<link rel="stylesheet" href="https://fonts.googleapis.com/css2?family=Inter:ital,wght@0,600;0,700;0,800;1,600&display=swap">
<style>
  :root {
    --cover-yellow: #fbbe2e;
    --emblem-yellow: #f5b228;
    --ink: #111111;
    --accent-orange: #ee7a00;
  }
  * { margin: 0; padding: 0; box-sizing: border-box; }
  html, body {
    width: 750px;
    height: 1200px;
    overflow: hidden;
    background: var(--cover-yellow);
  }
  .cover {
    position: relative;
    width: 750px;
    height: 1200px;
    background: var(--cover-yellow);
    font-family: "Inter", "Helvetica Neue", Arial, sans-serif;
    color: var(--ink);
    overflow: hidden;
  }
  .backdrop-emblem {
    position: absolute;
    left: 62px;
    top: 190px;
    width: 642px;
    height: 642px;
    border-radius: 50%;
    background: radial-gradient(circle, var(--emblem-yellow) 0%, var(--emblem-yellow) 55%, rgba(245,178,40,0) 72%);
  }
  .machine-illustration {
    position: absolute;
    left: 62px;
    top: 436px;
    width: 250px;
    height: 296px;
    border-radius: 40px;
    background: radial-gradient(ellipse at 60% 40%, var(--accent-orange) 0%, rgba(238,122,0,0.55) 55%, rgba(238,122,0,0) 78%);
  }
  .device-illustration {
    position: absolute;
    left: 463px;
    top: 295px;
    width: 86px;
    height: 56px;
    border-radius: 10px;
    background: linear-gradient(160deg, var(--cover-yellow), var(--accent-orange));
  }
  .title-block {
    position: absolute;
    left: 160px;
    top: 470px;
    width: 480px;
    transform-origin: left top;
    transform: skewY(-30deg);
    text-transform: uppercase;
    font-weight: 800;
    line-height: 0.92;
    letter-spacing: -0.02em;
  }
  .title-line { display: block; white-space: nowrap; }
  .title-line--one   { font-size: 42px; padding-left: 50px; }
  .title-line--two   { font-size: 50px; padding-left: 80px; }
  .title-line--three { font-size: 64px; padding-left: 110px; }
  .title-line--four  { font-size: 68px; padding-left: 100px; }
  .subtitle {
    display: block;
    margin-top: 10px;
    padding-left: 125px;
    font-size: 18px;
    font-style: italic;
    font-weight: 600;
    text-transform: none;
    letter-spacing: 0.01em;
  }
  .author {
    position: absolute;
    left: 0;
    right: 0;
    top: 1132px;
    text-align: center;
    font-size: 24px;
    font-weight: 600;
    letter-spacing: 0.005em;
  }
</style>
</head>
<body>
  <main class="cover">
    <div class="backdrop-emblem" role="img" aria-label="Large faint gear emblem in a slightly deeper yellow behind the title"></div>
    <div class="machine-illustration" role="img" aria-label="Isometric illustration of orange gears, small tablet tiles and a looping cable with a plug"></div>
    <div class="device-illustration" role="img" aria-label="Small isometric tablet device resting on the title"></div>

    <h1 class="title-block">
      <span class="title-line title-line--one">Lessons</span>
      <span class="title-line title-line--two">From the</span>
      <span class="title-line title-line--three">Silent</span>
      <span class="title-line title-line--four">Orchard</span>
      <span class="subtitle">mindset - insights - skills &amp; tools</span>
    </h1>

    <p class="author">Maarten de Klerk</p>
  </main>
</body>
</html>
```